NOTE: I PROVIDED THE INCORRECT LOGO AND ONLY A HANDFUL OF PEOPLE NOTICED THAT IT WAS NOT THE ONE I DESCRIBED. THE LOGO I HAVE NOW ATTACHED MATCHES MY WEBSITE AND THE COLORS ON THE WEBSITE SHOULD BE USED FOR THE CARD.

PLEASE READ THE BUSINESS CARD DETAILS AND PROJECT MUST HAVES CAREFULLY.

I am looking for a business card that is powerful, a bit edgy, and although I work in the corporate world, not too formal. I would like to see designs that use the colors on my website www.brightmoorlane.com. I don't want the card to look washed out so please use shades of those colors that make them "pop". The "vibe" of the card needs to show substance and confidence while also reflecting that we're not your usual consultants.

The focus of my work is turning "people problems" into profits. Those problems could be poor service, an unstable workforce, untrained leaders, or managing change. We are an aggressive, results-focused team of performance improvement professionals who refuse to believe "things can't be done". For us, failure is not an option. Our logo reflects a target from the view of the site on a gun.

In addition to the contact information provided on the sample business card (do not include "turning people problems into profits"), I would like to include this statement (probably on the back):
I equip results-oriented business leaders to turn their people problems into profits in six months or less.

PLEASE NOTE THAT MY WEBSITE IS UNDER REVISION TO TONE DOWN THE MILITARY THEME, ALTHOUGH THE WARRIOR ENERGY AND FOCUS ON RESULTS REMAINS.

Target Market(s)

My clients are Mid and senior-level managers. I don't target any particular industry.

Industry/Entity Type

Consulting

Contact Information for Business Card

In addition to the contact information provided on the sample business card (DO NOT INCLUDE "turning people problems into profits"), I would like to include this statement (probably on the back):

I don't care whether the card is landscape or portrait view.

Font styles to use
Sans Serif

Requirements
Must have
• 1. be easy to read, no 6-8 point fonts!
• 2. a "vibe" that captures the eye without being too chaotic or busy
• 3. bold color, not washed out or boring - a good blend with the colors currently on my website (black, red, white, army green) but you don't need to use all of them.
• 4. all the contact information I have provided
• 5. a good blend with the colors currently on my website
• 6. Must have this quote on the back of the card: I equip results-oriented business leaders to turn their people problems into profits in six months or less.
Nice to have
• In looking at the sample images I provided for ideas, you can see that I like the way a card carries over from one side to the next.
• It would be great to find some aspect/quality/feature that I haven't seen before
Should not have
• 1. NO use of ALL CAPS
• 2. fonts that I would have to seek out and purchase (you should provide files for font if using something not standard)

```html
<!DOCTYPE html>
<html lang="en">
<head>
<meta charset="utf-8">
<title>Brightmoor Lane – Business Card</title>
<link rel="stylesheet" href="https://fonts.googleapis.com/css2?family=Archivo+Black&family=Lato:wght@400;700&display=swap">
<style>
  :root {
    --bg: #8a8a8a;
    --red: #ec4136;
    --charcoal: #2f2e2f;
    --white: #ffffff;
    --muted: #cfcfcf;
  }
  * { box-sizing: border-box; margin: 0; padding: 0; }
  html, body { width: 1200px; height: 1200px; overflow: hidden; }
  body {
    background: var(--bg);
    font-family: "Lato", "Gill Sans", sans-serif;
    position: relative;
  }
  .card {
    position: absolute;
    left: 250px;
    width: 700px;
    height: 400px;
    box-shadow: 0 10px 28px rgba(0,0,0,0.28);
  }
  .card--front { top: 150px; background: var(--red); color: var(--white); }
  .card--back { top: 630px; background: var(--charcoal); color: var(--white); }

  .brand {
    position: absolute;
    left: 90px;
    top: 110px;
    display: flex;
    align-items: center;
    gap: 22px;
  }
  .brand__dot {
    width: 70px; height: 70px; border-radius: 50%;
    background: var(--white);
    flex: none;
  }
  .brand__name {
    font-family: "Archivo Black", "Arial Black", sans-serif;
    font-size: 64px;
    line-height: 1;
    color: var(--white);
  }
  .statement {
    position: absolute;
    left: 100px;
    right: 80px;
    top: 250px;
    font-size: 21px;
    line-height: 1.35;
  }

  .mark {
    position: absolute;
    left: 110px;
    top: 110px;
    width: 180px;
    height: 180px;
    border-radius: 50%;
    background: var(--white);
  }
  .details {
    position: absolute;
    left: 350px;
    top: 70px;
  }
  .details__name {
    font-family: "Archivo Black", "Arial Black", sans-serif;
    font-size: 34px;
    line-height: 1.1;
  }
  .details__title {
    color: var(--red);
    font-size: 20px;
    margin-top: 4px;
  }
  .contact {
    list-style: none;
    margin-top: 30px;
  }
  .contact__item {
    display: flex;
    align-items: center;
    gap: 14px;
    font-size: 21px;
    line-height: 1.5;
  }
  .contact__icon {
    width: 20px; height: 20px;
    flex: none;
    stroke: var(--muted);
    fill: none;
    stroke-width: 1.4;
  }
</style>
</head>
<body>

<section class="card card--front" aria-label="Card front">
  <div class="brand">
    <span class="brand__dot"></span>
    <span class="brand__name">Brightmoor<br>Lane</span>
  </div>
  <p class="statement">“I equip results-focused business leaders to turn their people problems into profits in six months or less.”</p>
</section>

<section class="card card--back" aria-label="Card back">
  <span class="mark"></span>
  <div class="details">
    <h1 class="details__name">Dana Whitfield</h1>
    <p class="details__title">Chief Performance Strategist</p>
    <ul class="contact">
      <li class="contact__item">
        <svg class="contact__icon" viewBox="0 0 20 20"><rect x="5" y="1.5" width="10" height="17" rx="1.5"/><line x1="8.5" y1="15.5" x2="11.5" y2="15.5"/></svg>
        555-014-2290
      </li>
      <li class="contact__item">
        <svg class="contact__icon" viewBox="0 0 20 20"><path d="M4 3 L7 3 L8.5 7 L6.5 8.5 C7.5 11 9 12.5 11.5 13.5 L13 11.5 L17 13 L17 16 C17 17 16 17.5 15 17.5 C8.5 17 3 11.5 2.5 5 C2.5 4 3 3 4 3 Z"/></svg>
        555-014-7718
      </li>
      <li class="contact__item">
        <svg class="contact__icon" viewBox="0 0 20 20"><rect x="2" y="4.5" width="16" height="11"/><polyline points="2,4.5 10,11 18,4.5"/></svg>
        danaw@brightmoorlane.com
      </li>
      <li class="contact__item">
        <svg class="contact__icon" viewBox="0 0 20 20"><polyline points="2,10 10,3 18,10"/><polyline points="4.5,8 4.5,17 15.5,17 15.5,8"/><rect x="8.5" y="12" width="3" height="5"/></svg>
        www.brightmoorlane.com
      </li>
    </ul>
  </div>
</section>

</body>
</html>
```